Tallow Bodyweight Gym Website

We need a website design for our gym.

Tallow is the UAE's first calisthenics and parkour gym. The theme under which the gym revolves is that one does not require any machinery to workout as our bodies could be themselves the machinery. The gym is designed to be the more of a social hub rather than an "in-and-out" gym, where people come train, have fun, hang out and socialize for a few hours rather than just train for 60 minutes then leave. The gym is designed to be a big open space with lots of natural sunlight, natural wood and plants all over the place to create a natural and refreshing setting. We also use recycled material throughout the gym and recycle our waste as being green is part of our philosophy. We currently also have some of the world's top and most recognized calisthenics athletes working with us.

We would like our website to reflect all that as well as provide a simple, interactive and fun way for visitors to be able to get class and gym information, check out gym media and contact us for bookings.

Target Market(s)

Ages 15-35

Industry/Entity Type

Fitness

Coding

Coded - Design and coding required

Number of Pages Required

4 page

Font styles to use
Decorative

Colors
0792cd

Requirements
Must have
• Class descriptions
• Gym description
• Class schedules
• Trainer profiles
• Gym philosophy
• Contact Details
Nice to have
• A link to contact us directly for a free first trial class

```html
<!DOCTYPE html>
<html lang="en">
<head>
<meta charset="utf-8">
<title>Tallow Bodyweight Gym</title>
<link rel="stylesheet" href="https://fonts.googleapis.com/css2?family=Ropa+Sans&family=Ubuntu:wght@500;700&family=Montserrat:wght@700&family=Lato:wght@100;300;900&family=Open+Sans:ital,wght@0,400;0,600;0,700;1,400&display=swap">
<style>
:root{
  --blue:#0792cd;
  --sky:#2aa3e3;
  --cyan:#27b5e4;
  --ink:#1d1d1d;
  --text:#333;
  --darker:#1a1a1a;
  --white:#fff;
}
*{box-sizing:border-box;margin:0;padding:0}
html,body{width:1200px;height:3130px;overflow:hidden;background:var(--white)}
body{font-family:"Open Sans",Arial,sans-serif;color:var(--text)}
.canvas{position:relative;width:1200px;height:3130px;overflow:hidden}

/* hero */
.hero{position:absolute;left:0;top:0;width:1200px;height:724px;
  background:
    radial-gradient(ellipse 240px 300px at 560px 330px,rgba(190,150,120,.55),transparent 70%),
    radial-gradient(ellipse 300px 200px at 230px 560px,rgba(40,110,160,.45),transparent 70%),
    radial-gradient(ellipse 260px 180px at 1000px 180px,rgba(120,140,150,.45),transparent 70%),
    radial-gradient(ellipse 400px 160px at 600px 680px,rgba(120,150,190,.35),transparent 70%),
    linear-gradient(100deg,#1f2124 0%,#3c352d 28%,#5b5246 48%,#343a41 72%,#1d2126 100%)}
.topbar{position:absolute;left:0;top:0;width:1200px;height:46px;background:rgba(20,20,20,.88)}
.topbar .contact{position:absolute;top:13px;font-size:14px;color:#eee;display:flex;align-items:center;gap:8px}
.icons{display:flex;gap:9px;align-items:center}
.topbar .icons{position:absolute;right:48px;top:17px}
.topbar .icons span{width:9px;height:9px;border:1.5px solid #cfcfcf;border-radius:2px}

.nav{position:absolute;left:50px;top:46px;width:1102px;height:96px;background:var(--white)}
.brand{position:absolute;left:22px;top:28px;display:flex;align-items:center;gap:10px;
  font-family:"Ubuntu",sans-serif;font-weight:700;font-size:30px;color:var(--ink)}
.brand i{width:16px;height:16px;border-radius:50%;background:var(--blue);display:block}
.nav ul{list-style:none}
.nav li{position:absolute;top:40px;transform:translateX(-50%);font-family:"Montserrat",sans-serif;
  font-weight:700;font-size:13px;color:var(--ink);white-space:nowrap}
.nav li.active{color:var(--blue)}
.nav li.active::before{content:"";position:absolute;left:-10px;right:-10px;top:-40px;height:5px;background:var(--blue)}

.hero-panel{position:absolute;left:676px;top:246px;width:476px;height:301px;background:rgba(10,14,20,.72);padding:28px 26px}
.hero-panel h2{font-family:"Ubuntu",sans-serif;font-weight:700;color:var(--white);font-size:29px;line-height:1}
.hero-panel h1{font-family:"Ubuntu",sans-serif;font-weight:700;color:var(--cyan);font-size:43px;line-height:48px;margin-top:14px}
.hero-panel p{color:#e8e8e8;font-size:12px;line-height:19px;margin-top:12px}
.btn{display:inline-block;background:var(--blue);color:var(--white);font-weight:700;font-size:13px;padding:11px 14px}
.hero-panel .btn{margin-top:16px}

.sec-title{position:absolute;right:52px;text-align:right}
.sec-title h3{font-family:"Ropa Sans",sans-serif;font-weight:400;font-size:40px;color:var(--ink);line-height:1}
.sec-title p{font-family:Arial,sans-serif;font-size:14px;color:var(--ink);margin-top:6px}

/* features */
.feature{position:absolute;top:855px;width:305px;text-align:center}
.feature .bar-top{position:absolute;top:0;left:19px;width:263px;height:24px;background:var(--sky)}
.feature .bar-bottom{position:absolute;top:226px;left:19px;width:263px;height:25px;background:var(--sky)}
.feature .photo{position:absolute;top:24px;left:0;width:305px;height:202px}
.feature h4{position:absolute;top:268px;left:0;width:100%;font-family:"Ropa Sans",sans-serif;font-weight:400;font-size:29px;color:var(--ink)}
.feature p{position:absolute;top:312px;left:-5px;width:315px;font-family:Arial,sans-serif;font-size:16px;line-height:21px;color:var(--ink)}

/* philosophy */
.philosophy{position:absolute;left:0;top:1315px;width:1200px;height:480px;
  background:
    radial-gradient(ellipse 200px 260px at 320px 230px,rgba(200,150,120,.55),transparent 70%),
    radial-gradient(ellipse 160px 120px at 240px 70px,rgba(120,90,70,.6),transparent 70%),
    linear-gradient(90deg,#2f2620 0%,#5e4a3b 20%,#8e7560 38%,#cdb9a2 55%,#ece2d4 75%,#f3ece2 100%)}
.philosophy .copy{position:absolute;right:50px;top:171px;width:520px;text-align:right;font-size:13px;line-height:21px;color:var(--ink)}
.philosophy .copy p+p{margin-top:20px}
.philosophy .btn{position:absolute;right:50px;top:380px}

/* trainers */
.trainer{position:absolute;top:1976px;width:336px;height:357px}
.trainer .photo{position:absolute;left:0;top:0;width:269px;height:357px}
.trainer .strip{position:absolute;right:0;top:0;width:67px;height:357px;background:var(--sky)}
.trainer .strip span{position:absolute;left:27px;width:13px;height:13px;border:2px solid var(--white);border-radius:3px}
.trainer .bio{position:absolute;left:6px;top:6px;width:257px;height:345px;background:rgba(70,70,70,.85);padding:34px 26px;color:var(--white)}
.trainer .bio h5{font-family:"Montserrat",sans-serif;font-weight:700;font-size:15px}
.trainer .bio em{display:block;font-size:12px;margin-top:4px}
.trainer .bio p{font-weight:700;font-size:12px;line-height:19px;margin-top:20px}

/* footer */
.pushup{position:absolute;left:428px;top:2442px;width:344px;height:152px;
  background:
    radial-gradient(ellipse 70px 60px at 172px 110px,rgba(150,110,85,.9),transparent 75%),
    radial-gradient(ellipse 160px 40px at 172px 60px,rgba(170,130,100,.7),transparent 75%),
    linear-gradient(180deg,#fff 0%,#fff 20%,#efe9e4 100%)}
.footer{position:absolute;left:0;top:2594px;width:1200px;height:484px;
  background:
    radial-gradient(ellipse 140px 260px at 60px 160px,rgba(90,70,55,.55),transparent 75%),
    linear-gradient(90deg,#1f1f1f 0%,#2d2d2d 25%,#2d2d2d 100%)}
.footer .brand-foot{position:absolute;left:0;width:1200px;top:30px;text-align:center;font-family:"Ubuntu",sans-serif;font-weight:700;font-size:22px;color:var(--white)}
.footer .brand-foot i{display:inline-block;width:10px;height:10px;border-radius:50%;background:var(--blue);margin-right:8px;vertical-align:middle}
.footer .kicker{position:absolute;left:0;width:1200px;top:74px;text-align:center;font-family:"Lato",sans-serif;font-weight:300;font-size:22px;color:#6d6d6d;letter-spacing:1px}
.footer .phone{position:absolute;left:0;width:1200px;top:100px;text-align:center;font-family:"Lato",sans-serif;font-size:86px;color:var(--white);letter-spacing:-1px}
.thin{font-weight:100}.bold{font-weight:900}
.footer .rule{position:absolute;left:223px;width:806px;top:203px;height:1px;background:#444}
.col{position:absolute;top:247px}
.col h6{font-family:"Lato",sans-serif;font-weight:900;font-size:17px;color:var(--white);letter-spacing:-.3px}
.col p{font-size:12px;line-height:19px;color:#ddd;margin-top:18px;width:230px}
.col ul{list-style:none;margin-top:48px}
.col li{font-size:10px;color:#ddd;display:flex;align-items:center;gap:10px;height:22px}
.news{display:flex;gap:14px;margin-top:14px}
.news .thumb{width:66px;height:46px;flex:none}
.news b{display:block;font-family:"Lato",sans-serif;font-weight:900;font-size:12px;color:var(--white);line-height:17px;width:170px;border-bottom:1px solid #555;padding-bottom:3px}
.news small{font-size:9px;color:#999}
.trial{position:absolute;left:770px;top:2880px;width:257px;height:167px;
  background:
    radial-gradient(ellipse 60px 50px at 70px 50px,rgba(200,160,130,.8),transparent 75%),
    radial-gradient(ellipse 70px 50px at 160px 110px,rgba(220,180,150,.8),transparent 75%),
    linear-gradient(180deg,#ebe7e2 0%,#dcd6cf 60%,#6fb2dd 80%,#4a9ed4 100%)}
.bottom{position:absolute;left:0;top:3078px;width:1200px;height:52px;background:var(--darker)}
.bottom p{position:absolute;left:67px;top:18px;font-size:13px;color:#aaa}
.bottom .icons{position:absolute;left:887px;top:15px;gap:8px}
.bottom .icons span{width:22px;height:22px;background:var(--white);position:relative}
.bottom .icons span::after{content:"";position:absolute;left:7px;top:7px;width:8px;height:8px;border-radius:50%;background:#333}
</style>
</head>
<body>
<div class="canvas">

  <header>
    <div class="hero" role="img" aria-label="Athlete performing a one-arm hold on a pull-up bar inside the gym"></div>
    <div class="topbar">
      <div class="contact" style="left:596px">
        <svg width="14" height="14" viewBox="0 0 24 24"><path fill="#eee" d="M6.6 10.8a15 15 0 006.6 6.6l2.2-2.2a1 1 0 011-.25 11.4 11.4 0 003.6.57 1 1 0 011 1V20a1 1 0 01-1 1A17 17 0 013 4a1 1 0 011-1h3.5a1 1 0 011 1c0 1.25.2 2.45.57 3.57a1 1 0 01-.25 1z"/></svg>
        1300 555 014
      </div>
      <div class="contact" style="left:766px">
        <svg width="22" height="14" viewBox="0 0 22 14"><rect x="1" y="1" width="20" height="12" fill="none" stroke="#eee" stroke-width="1.5"/><path d="M1 1l10 7 10-7" fill="none" stroke="#eee" stroke-width="1.5"/></svg>
        contact@tallow-gym.com
      </div>
      <div class="icons"><span></span><span></span><span></span><span></span><span></span><span></span></div>
    </div>
    <nav class="nav">
      <div class="brand"><i></i>Tallow</div>
      <ul>
        <li class="active" style="left:301px">HOME</li>
        <li style="left:409px">ABOUT US</li>
        <li style="left:522px">CLASSES</li>
        <li style="left:632px">TRAINERS</li>
        <li style="left:739px">EVENT</li>
        <li style="left:847px">ELEMENTS</li>
        <li style="left:952px">SHOP</li>
        <li style="left:1056px">CONTACT</li>
      </ul>
    </nav>
    <div class="hero-panel">
      <h2>GET HOME WITH</h2>
      <h1>CHECK OF A BODY<br>LIKE ADONIS</h1>
      <p>Core Motion is a complete sports/fitness theme that is suitable for any one who is about to start a Fitness Center or a Sports Website. Have a look and enjoy the Exclusive Features of a Fitness Website.</p>
      <a class="btn">ENROLL NOW</a>
    </div>
  </header>

  <section>
    <div class="sec-title" style="top:756px"><h3>Gym description</h3><p>Lorem Ipsum is simply dummy text of the printing</p></div>
    <div class="feature" style="left:69px">
      <div class="bar-top"></div>
      <div class="photo" role="img" aria-label="Woman standing in a training hall" style="background:radial-gradient(ellipse 60px 90px at 190px 120px,rgba(225,190,165,.9),transparent 75%),radial-gradient(ellipse 90px 70px at 60px 60px,rgba(120,150,90,.8),transparent 75%),linear-gradient(120deg,#5f6f55,#a9a89c 50%,#2f2d2b)"></div>
      <div class="bar-bottom"></div>
      <h4>Class Description</h4>
      <p>Find a trainer, professional athletes, calisthenics &amp; parkour gym</p>
    </div>
    <div class="feature" style="left:455px">
      <div class="bar-top"></div>
      <div class="photo" role="img" aria-label="Trainer guiding a client with a kettlebell" style="background:radial-gradient(ellipse 50px 80px at 130px 140px,rgba(230,90,140,.7),transparent 75%),radial-gradient(ellipse 60px 100px at 220px 110px,rgba(40,40,45,.85),transparent 75%),linear-gradient(180deg,#8aa4bb,#e4e6e8 45%,#7e7873)"></div>
      <div class="bar-bottom"></div>
      <h4>Gym Description</h4>
      <p>Find a trainer, professional athletes, calisthenics &amp; parkour gym</p>
    </div>
    <div class="feature" style="left:829px">
      <div class="bar-top"></div>
      <div class="photo" role="img" aria-label="Group class lifting dumbbells" style="background:radial-gradient(ellipse 60px 90px at 80px 120px,rgba(200,150,120,.9),transparent 75%),radial-gradient(ellipse 90px 70px at 210px 80px,rgba(40,80,160,.85),transparent 75%),linear-gradient(180deg,#cfd3d8,#a58c78 70%,#6a5546)"></div>
      <div class="bar-bottom"></div>
      <h4>Class Schedules</h4>
      <p>Find a trainer, professional athletes, calisthenics &amp; parkour gym</p>
    </div>
  </section>

  <section class="philosophy" role="img" aria-label="Athlete wrapping hand tape against a textured wall">
    <div class="sec-title" style="top:56px;right:50px"><h3>Gym philosophy</h3><p>Lorem Ipsum is simply dummy text of the printing</p></div>
    <div class="copy">
      <p>Lorem ipsum dolor sit amet, consectetuer adipiscing elit. Aenean commodo ligula eget dolor. Aenean massa. Cum sociis natoque penatibus et magnis dis parturient montes, nascetur ridiculus mus. Donec quam felis, ultricies nec, pellentesque eu, pretium quis, sem.</p>
      <p>Phasellus dignissim arcu neque, non porta leo molestie eu. Nam id condimentum lectus. Proin placerat sed urna nec convallis. Morbi vitae odio congue, laoreet risus ut, commodo sapien.</p>
    </div>
    <a class="btn">ENROLL NOW</a>
  </section>

  <section>
    <div class="sec-title" style="top:1858px"><h3>Trainer profiles</h3><p>Lorem Ipsum is simply dummy text of the printing</p></div>
    <div class="trainer" style="left:75px">
      <div class="photo" role="img" aria-label="Trainer portrait in a dark gym" style="background:radial-gradient(ellipse 120px 160px at 130px 200px,rgba(140,60,60,.6),transparent 75%),linear-gradient(160deg,#4a3432,#221e1e)"></div>
      <div class="bio">
        <h5>MAREK DOVLAN</h5>
        <em>Bodybuilding Instructor</em>
        <p>A wonderful serenity has taken possession of my entire soul, like these sweet mornings of spring which I enjoy with my whole heart. I am alone, and feel the charm of existence.</p>
      </div>
      <div class="strip"><span style="top:22px"></span><span style="top:61px"></span><span style="top:100px"></span><span style="top:139px"></span></div>
    </div>
    <div class="trainer" style="left:438px">
      <div class="photo" role="img" aria-label="Trainer working with weights" style="background:radial-gradient(ellipse 90px 120px at 170px 150px,rgba(160,80,50,.85),transparent 75%),radial-gradient(ellipse 80px 90px at 60px 260px,rgba(120,120,120,.6),transparent 75%),linear-gradient(160deg,#3c3c3c,#2a2622)"></div>
      <div class="strip"><span style="top:22px"></span><span style="top:61px"></span><span style="top:100px"></span><span style="top:139px"></span></div>
    </div>
    <div class="trainer" style="left:803px">
      <div class="photo" role="img" aria-label="Trainer posing in sports wear" style="background:radial-gradient(ellipse 80px 70px at 135px 80px,rgba(220,190,130,.8),transparent 75%),radial-gradient(ellipse 120px 120px at 135px 220px,rgba(200,140,110,.85),transparent 75%),linear-gradient(160deg,#4e4a46,#2f2c2a)"></div>
      <div class="strip"><span style="top:22px"></span><span style="top:61px"></span><span style="top:100px"></span><span style="top:139px"></span></div>
    </div>
  </section>

  <div class="pushup" role="img" aria-label="Athlete in a push-up position"></div>

  <footer class="footer">
    <div class="brand-foot"><i></i>Tallow</div>
    <div class="kicker">CONTACT US ANYTIME</div>
    <div class="phone"><span class="thin">+61</span><span class="bold">-555-010-</span><span class="thin">742</span></div>
    <div class="rule"></div>

    <div class="col" style="left:223px">
      <h6>ABOUT US</h6>
      <p>Come in and see our impressive club, guaranteed to impress</p>
      <ul>
        <li><svg width="10" height="8" viewBox="0 0 10 8"><rect x=".5" y=".5" width="9" height="7" fill="none" stroke="#ddd"/><path d="M.5.5l4.5 4 4.5-4" fill="none" stroke="#ddd"/></svg>EMAIL@EXAMPLE.COM</li>
        <li><svg width="10" height="10" viewBox="0 0 24 24"><path fill="#ddd" d="M6.6 10.8a15 15 0 006.6 6.6l2.2-2.2a1 1 0 011-.25 11.4 11.4 0 003.6.57 1 1 0 011 1V20a1 1 0 01-1 1A17 17 0 013 4a1 1 0 011-1h3.5a1 1 0 011 1c0 1.25.2 2.45.57 3.57a1 1 0 01-.25 1z"/></svg>+61-555-010-742</li>
        <li><svg width="8" height="11" viewBox="0 0 8 11"><path fill="#ddd" d="M4 0a4 4 0 00-4 4c0 3 4 7 4 7s4-4 4-7a4 4 0 00-4-4zm0 5.5A1.5 1.5 0 114 2.5a1.5 1.5 0 010 3z"/></svg>HARBOURSIDE, COASTLINE</li>
      </ul>
    </div>

    <div class="col" style="left:499px">
      <h6>LATEST NEWS</h6>
      <div class="news" style="margin-top:22px">
        <div class="thumb" role="img" aria-label="Class training outdoors" style="background:radial-gradient(ellipse 18px 18px at 40px 22px,rgba(220,180,150,.9),transparent 75%),linear-gradient(180deg,#b9d0dd,#8fb8cc 70%,#c8a88e)"></div>
        <div><b>EXCITING NEW<br>CLASSES</b><small>7 COMMENTS &nbsp; 22 AUG 2014</small></div>
      </div>
      <div class="news">
        <div class="thumb" role="img" aria-label="Athlete on a bench press" style="background:radial-gradient(ellipse 20px 14px at 30px 26px,rgba(200,150,120,.9),transparent 75%),linear-gradient(135deg,#4d4038,#8a7464)"></div>
        <div><b>BENCH PRESS<br>COMPETITION</b><small>25 COMMENTS &nbsp; 03 JUL 2014</small></div>
      </div>
    </div>

    <div class="col" style="left:770px"><h6>NEW PERSONAL TRAINER</h6></div>
  </footer>
  <div class="trial" role="img" aria-label="New personal trainer coaching a client on a mat"></div>

  <div class="bottom">
    <p>Copyright © 2015 – Tallow Bodyweight Gym – All rights reserved.</p>
    <div class="icons"><span></span><span></span><span></span><span></span><span></span></div>
  </div>

</div>
</body>
</html>
```